Conceptual Model Diagram for Replacing Medication with Behavior to Support Weight Loss Maintenance

Design a figure of a conceptual model that needs to be inserted into a word document for a PSF grant. This conceptual model illustrates how behavioral strategies can replace the regulatory functions lost after AOM discontinuation. The intervention targets three core vulnerabilities—appetite resurgence, metabolic inflexibility, and suboptimal mindstate—through the domains of Food, Physical Activity, and Mind. Sustained weight loss maintenance occurs at the intersection of these domains. The intervention is delivered within a design framework that makes behaviors easier to perform, aligns them with identity, and reinforces them through virtual support and community, ensuring real-world feasibility and long-term adherence.
Target Market(s)
PSF reviewers
Industry/Entity Type
academic
Other font styles liked:
- arial
Requirements
Must have
- see my attached description

```html
<!DOCTYPE html>
<html lang="en">
<head>
<meta charset="utf-8">
<title>Conceptual Model for Replacing Medication with Behavior to Support Weight Loss Maintenance</title>
<link rel="stylesheet" href="https://fonts.googleapis.com/css2?family=Anton&family=Arimo:wght@400;700&display=swap">
<style>
  :root {
    --bg: #ffffff;
    --title: #454545;
    --ring-identity: #7a7a7a;
    --ring-easy: #b5b5b5;
    --ring-support: #4a4a4a;
    --domain: #8a8a8a;
    --overlap: #444444;
    --core: #232323;
    --stroke: #111111;
    --callout: #cfcfcf;
    --ink: #111111;
    --light: #ffffff;
  }
  html, body {
    margin: 0;
    padding: 0;
    background: var(--bg);
    overflow: hidden;
  }
  .figure {
    position: relative;
    width: 1200px;
    height: 927px;
    background: var(--bg);
    overflow: hidden;
  }
  .figure-title {
    position: absolute;
    top: 72px;
    left: 0;
    width: 1200px;
    margin: 0;
    text-align: center;
    font-family: "Anton", "Oswald", sans-serif;
    font-weight: 400;
    font-size: 42px;
    line-height: 48px;
    color: var(--title);
    letter-spacing: 0.2px;
  }
  .model {
    position: absolute;
    top: 0;
    left: 0;
  }
  .ring-title { font-family: "Arimo", Arial, sans-serif; font-weight: 700; font-size: 20px; fill: var(--light); }
  .ring-note { font-family: "Arimo", Arial, sans-serif; font-weight: 400; font-size: 14.5px; fill: var(--light); }
  .ring-note-bottom { font-family: "Arimo", Arial, sans-serif; font-weight: 400; font-size: 13.5px; fill: var(--light); }
  .domain-label { font-family: "Arimo", Arial, sans-serif; font-weight: 700; font-size: 21px; fill: var(--light); }
  .core-label { font-family: "Arimo", Arial, sans-serif; font-weight: 400; font-size: 13.5px; fill: var(--light); }
  .callout-box { fill: var(--callout); }
  .callout-text { font-family: "Arimo", Arial, sans-serif; font-weight: 400; font-size: 13.5px; fill: var(--ink); }
  .circle-outline { fill: none; stroke: var(--stroke); stroke-width: 1.4; }
  .arrow { stroke: var(--ink); stroke-width: 1.6; fill: none; }
</style>
</head>
<body>
<div class="figure">
  <h1 class="figure-title">Conceptual Model for Replacing Medication<br>with Behavior to Support Weight Loss Maintenance</h1>

  <svg class="model" width="1200" height="927" viewBox="0 0 1200 927" xmlns="http://www.w3.org/2000/svg">
    <defs>
      <clipPath id="clip-food"><circle cx="602" cy="460" r="115"/></clipPath>
      <clipPath id="clip-activity"><circle cx="540" cy="600" r="115"/></clipPath>
      <clipPath id="clip-mind"><circle cx="660" cy="600" r="115"/></clipPath>
      <marker id="arrowhead" viewBox="0 0 10 10" refX="9" refY="5" markerWidth="8" markerHeight="8" orient="auto">
        <path d="M0,0 L10,5 L0,10 z" fill="#111"/>
      </marker>
      <path id="path-identity" d="M 336.6 664.3 A 293 293 0 0 1 598 243"/>
      <path id="path-easy" d="M 604 243 A 293 293 0 0 1 863.4 664.3"/>
      <path id="path-support" d="M 369.4 729.5 A 301 301 0 0 0 830.6 729.5"/>
      <path id="path-support-note" d="M 356.4 740.5 A 318 318 0 0 0 843.6 740.5"/>
    </defs>

    <!-- framework ring -->
    <g class="framework-ring" fill="none">
      <path d="M 327.1 670.0 A 303 303 0 0 1 597 233" stroke="var(--ring-identity)" stroke-width="30"/>
      <path d="M 603 233 A 303 303 0 0 1 872.9 670.0" stroke="var(--ring-easy)" stroke-width="30"/>
      <path d="M 873.1 677.0 A 305 305 0 0 1 326.9 677.0" stroke="var(--ring-support)" stroke-width="44"/>
    </g>

    <text class="ring-title"><textPath href="#path-identity" startOffset="8">Align with Identity</textPath></text>
    <text class="ring-note"><textPath href="#path-identity" startOffset="200">(self-concept, Maintain IT model, internalization)</textPath></text>

    <text class="ring-title"><textPath href="#path-easy" startOffset="34">Make it Easy</textPath></text>
    <text class="ring-note"><textPath href="#path-easy" startOffset="168">(habits, routines, environment, low friction)</textPath></text>

    <text class="ring-title"><textPath href="#path-support" startOffset="50%" text-anchor="middle">Virtual Support and Social Connection</textPath></text>
    <text class="ring-note-bottom"><textPath href="#path-support-note" startOffset="50%" text-anchor="middle">(accessibility, community, shared accountability)</textPath></text>

    <!-- domains venn -->
    <g class="domains">
      <circle cx="602" cy="460" r="115" fill="var(--domain)"/>
      <circle cx="540" cy="600" r="115" fill="var(--domain)"/>
      <circle cx="660" cy="600" r="115" fill="var(--domain)"/>
      <g clip-path="url(#clip-food)">
        <circle cx="540" cy="600" r="115" fill="var(--overlap)"/>
        <circle cx="660" cy="600" r="115" fill="var(--overlap)"/>
      </g>
      <g clip-path="url(#clip-activity)">
        <circle cx="660" cy="600" r="115" fill="var(--overlap)"/>
        <g clip-path="url(#clip-mind)">
          <circle cx="602" cy="460" r="115" fill="var(--core)"/>
        </g>
      </g>
      <circle class="circle-outline" cx="602" cy="460" r="115"/>
      <circle class="circle-outline" cx="540" cy="600" r="115"/>
      <circle class="circle-outline" cx="660" cy="600" r="115"/>

      <text class="domain-label" x="602" y="466" text-anchor="middle">Food</text>
      <text class="domain-label" x="490" y="628" text-anchor="middle">Physical</text>
      <text class="domain-label" x="490" y="654" text-anchor="middle">Activity</text>
      <text class="domain-label" x="704" y="648" text-anchor="middle">Mind</text>

      <text class="core-label" x="600" y="567" text-anchor="middle">Sustained</text>
      <text class="core-label" x="600" y="584" text-anchor="middle">Weight Loss</text>
      <text class="core-label" x="600" y="601" text-anchor="middle">Maintenance</text>
    </g>

    <!-- vulnerabilities -->
    <g class="vulnerability">
      <rect class="callout-box" x="549" y="300" width="102" height="35" rx="5"/>
      <text class="callout-text" x="600" y="314" text-anchor="middle">Appetite</text>
      <text class="callout-text" x="600" y="330" text-anchor="middle">Resurgence</text>
      <line class="arrow" x1="600" y1="343" x2="600" y2="386" marker-end="url(#arrowhead)"/>
    </g>
    <g class="vulnerability">
      <rect class="callout-box" x="366" y="432" width="102" height="35" rx="5"/>
      <text class="callout-text" x="417" y="446" text-anchor="middle">Metabolic</text>
      <text class="callout-text" x="417" y="462" text-anchor="middle">Inflexibility</text>
      <line class="arrow" x1="414" y1="473" x2="452" y2="512" marker-end="url(#arrowhead)"/>
    </g>
    <g class="vulnerability">
      <rect class="callout-box" x="734" y="432" width="102" height="35" rx="5"/>
      <text class="callout-text" x="785" y="446" text-anchor="middle">Suboptimal</text>
      <text class="callout-text" x="785" y="462" text-anchor="middle">Mindstate</text>
      <line class="arrow" x1="788" y1="474" x2="756" y2="514" marker-end="url(#arrowhead)"/>
    </g>
  </svg>
</div>
</body>
</html>
```